Brintell's Business Card

I need some designs for a new business card including the new logo attached. An old example of our business card is also attached to show all the data that should be included on the new design.
**I added some more examples someone had mocked up**

Contact Information for Business Card

Should include all info on other examples uploaded.

```html
<!DOCTYPE html>
<html lang="en">
<head>
<meta charset="utf-8">
<title>Brintell's Business Card</title>
<link href="https://fonts.googleapis.com/css2?family=Montserrat:wght@500;600;700&family=Oswald:wght@500&display=swap" rel="stylesheet">
<style>
  :root {
    --bg: #3a3a3a;
    --blue: #0a6ab3;
    --blue-deep: #075fa3;
    --red: #e3222b;
    --white: #ffffff;
  }
  * { margin: 0; padding: 0; box-sizing: border-box; }
  html, body { width: 1200px; height: 1200px; overflow: hidden; background: var(--bg); }
  .stage { position: relative; width: 1200px; height: 1200px; }
  .card {
    position: absolute; left: 160px; width: 880px; height: 503px;
    border-radius: 36px; overflow: hidden;
    box-shadow: 0 14px 30px rgba(0,0,0,.45);
  }
  .card-front { top: 70px; background: var(--white); }
  .card-back { top: 627px; background: var(--blue); }

  .front-brand {
    position: absolute; top: 0; left: 0; right: 0; height: 232px;
    display: flex; align-items: center; justify-content: center; gap: 22px;
  }
  .brand-dot { width: 58px; height: 58px; border-radius: 50%; background: var(--red); }
  .brand-name {
    font-family: "Montserrat", sans-serif; font-weight: 700;
    font-size: 82px; letter-spacing: 1px; color: var(--blue); line-height: 1;
  }
  .red-rule { position: absolute; top: 232px; left: 0; right: 0; height: 9px; background: var(--red); }
  .front-panel {
    position: absolute; top: 249px; left: 0; right: 0; bottom: 0;
    background: var(--blue); color: var(--white);
  }
  .contact { position: absolute; left: 70px; top: 42px; font-family: "Montserrat", sans-serif; }
  .contact-name { font-size: 30px; font-weight: 600; letter-spacing: 1px; margin-bottom: 16px; }
  .contact-row { display: flex; align-items: center; gap: 16px; font-size: 20px; font-weight: 500; height: 34px; }
  .contact-row svg { width: 22px; height: 22px; flex: none; }
  .divider { position: absolute; left: 460px; top: 40px; width: 1px; height: 170px; background: rgba(255,255,255,.45); }
  .credentials {
    position: absolute; left: 510px; top: 68px;
    font-family: "Oswald", sans-serif; font-weight: 500; font-size: 34px;
    line-height: 1.25; text-transform: uppercase; letter-spacing: .5px;
  }

  .back-brand {
    position: absolute; top: 170px; left: 0; right: 0;
    display: flex; align-items: center; justify-content: center; gap: 26px;
  }
  .back-brand .brand-name { color: var(--white); font-size: 96px; }
  .service-area {
    position: absolute; left: 0; right: 0; bottom: 56px; text-align: center;
    font-family: "Oswald", sans-serif; font-weight: 500; font-size: 34px;
    color: var(--white); text-transform: uppercase; letter-spacing: .5px;
  }
</style>
</head>
<body>
<main class="stage">
  <section class="card card-front">
    <div class="front-brand">
      <span class="brand-dot"></span>
      <span class="brand-name">BRINTELL'S</span>
    </div>
    <div class="red-rule"></div>
    <div class="front-panel">
      <div class="contact">
        <p class="contact-name">DALE BRINTELL</p>
        <p class="contact-row">
          <svg viewBox="0 0 24 24" fill="#fff"><path d="M6.6 10.8a15.1 15.1 0 0 0 6.6 6.6l2.2-2.2a1 1 0 0 1 1-.25 11.4 11.4 0 0 0 3.6.57 1 1 0 0 1 1 1V20a1 1 0 0 1-1 1A17 17 0 0 1 3 4a1 1 0 0 1 1-1h3.5a1 1 0 0 1 1 1c0 1.25.2 2.45.57 3.57a1 1 0 0 1-.25 1z"/></svg>
          555.014.2290
        </p>
        <p class="contact-row">
          <svg viewBox="0 0 24 24" fill="none" stroke="#fff" stroke-width="2"><rect x="2" y="5" width="20" height="14"/><path d="M2 5l10 8 10-8"/></svg>
          hvacbrintell@mailbox.com
        </p>
        <p class="contact-row">
          <svg viewBox="0 0 24 24" fill="none" stroke="#fff" stroke-width="1.6"><circle cx="12" cy="12" r="10"/><ellipse cx="12" cy="12" rx="4.5" ry="10"/><path d="M2 12h20M4 7h16M4 17h16"/></svg>
          www.brintellhvac.com
        </p>
      </div>
      <div class="divider"></div>
      <div class="credentials">
        <p>Licensed &amp; Insured</p>
        <p>Family Owned &amp; Operated</p>
      </div>
    </div>
  </section>

  <section class="card card-back">
    <div class="back-brand">
      <span class="brand-dot"></span>
      <span class="brand-name">BRINTELL'S</span>
    </div>
    <p class="service-area">Serves Maple Ridge, IA &amp; Surrounding Areas</p>
  </section>
</main>
</body>
</html>
```